We need a company profile design 8 + cover

The company profile is attached below, we need to renew the whole thing with full modification. content and page arrangement is the same. All should be A5 size printable and electronic copies.

I attached logo and colors for identity, please use logo colors as main scheme colours

We need 2 copies Arabic and English

Font styles to use
Sans Serif

Requirements
Nice to have
• Please let us know how we can use the designs to edit in Arabic

```html
<!DOCTYPE html>
<html lang="en">
<head>
<meta charset="utf-8">
<title>What We Do – Company Profile Spread</title>
<link href="https://fonts.googleapis.com/css2?family=Source+Sans+3:wght@400;600;700&display=swap" rel="stylesheet">
<style>
  :root {
    --navy: #1d2d66;
    --navy-deep: #182659;
    --ink: #1a1a1a;
    --paper: #ffffff;
    --backdrop: #bdbdbd;
    --on-navy: #ffffff;
    --on-navy-soft: #e6e9f3;
  }
  * { box-sizing: border-box; margin: 0; padding: 0; }
  html, body { width: 1200px; height: 986px; overflow: hidden; }
  body {
    background: var(--backdrop);
    font-family: "Source Sans 3", "Source Sans Pro", sans-serif;
    display: flex; align-items: center; justify-content: center;
  }
  .spread {
    width: 1160px; height: 410px;
    display: flex;
    box-shadow: 0 6px 18px rgba(0,0,0,.18);
  }
  .page { width: 580px; height: 410px; }
  .page--intro { background: var(--paper); color: var(--ink); padding: 27px 28px 0 28px; }
  .page--services { background: var(--navy); color: var(--on-navy); padding: 22px 24px 0 28px; }

  .page-title { color: var(--navy); font-size: 20px; font-weight: 600; line-height: 1; margin-bottom: 12px; }
  .intro { font-size: 10.6px; line-height: 1.13; text-align: justify; margin-bottom: 20px; }
  .brand { color: var(--navy); font-weight: 700; }

  .service { display: flex; gap: 8px; }
  .service-icon { flex: 0 0 34px; width: 34px; height: 34px; margin-top: 4px; }
  .service-name { font-size: 15.5px; font-weight: 600; line-height: 1.1; margin-bottom: 3px; }
  .service-text { font-size: 10.6px; line-height: 1.3; }

  .page--intro .service { margin-bottom: 14px; }
  .page--intro .service-name { color: var(--navy); }
  .page--intro .service-icon circle.disc { fill: var(--navy); }
  .page--intro .service-icon .glyph { stroke: var(--paper); }

  .page--services .service { margin-bottom: 12px; }
  .page--services .service-text { color: var(--on-navy-soft); }
  .page--services .service-icon circle.disc { fill: var(--paper); }
  .page--services .service-icon .glyph { stroke: var(--navy); }
  .glyph { fill: none; stroke-width: 1.4; stroke-linecap: round; stroke-linejoin: round; }
</style>
</head>
<body>
<main class="spread">
  <section class="page page--intro">
    <h1 class="page-title">What We Do</h1>
    <p class="intro"><span class="brand">CAMPUS PATH</span> offers professional consultation to local and international students on a wide variety of educational programs covering summer and English programs, pathway courses, undergraduate, post-graduate degree programs and PHD courses. We specialize in providing professional assistance to students of various age groups. We help students through each stage.</p>

    <div class="service">
      <svg class="service-icon" viewBox="0 0 34 34"><circle class="disc" cx="17" cy="17" r="17"/><g class="glyph"><rect x="10" y="11" width="14" height="9" rx="1"/><path d="M13 24h8M17 20v4M12 14h4M12 17h6"/></g></svg>
      <div><h2 class="service-name">FREE Academic Consulting</h2>
      <p class="service-text">We get to understand the student’s academic, social, and personal backgrounds and then provide them with various career options.</p></div>
    </div>
    <div class="service">
      <svg class="service-icon" viewBox="0 0 34 34"><circle class="disc" cx="17" cy="17" r="17"/><g class="glyph"><path d="M9 20l8 4 8-4M9 16l8 4 8-4M9 12l8-4 8 4-8 4z"/></g></svg>
      <div><h2 class="service-name">Course Selection</h2>
      <p class="service-text">We assist our students in finding them right and correct courses based on their interests. Courses that are suitable to the industry in uplifting their professional levels for a successful career.</p></div>
    </div>
    <div class="service">
      <svg class="service-icon" viewBox="0 0 34 34"><circle class="disc" cx="17" cy="17" r="17"/><g class="glyph"><rect x="11" y="9" width="12" height="16" rx="1"/><circle cx="17" cy="14" r="2"/><path d="M14 19h6M14 22h4"/></g></svg>
      <div><h2 class="service-name">Application Submission</h2>
      <p class="service-text">We help save the students’ time and energy by providing advice through the entire process of application. Providing assistance with the required documents, deadlines, and personal statement editing etc.</p></div>
    </div>
    <div class="service">
      <svg class="service-icon" viewBox="0 0 34 34"><circle class="disc" cx="17" cy="17" r="17"/><g class="glyph"><circle cx="17" cy="14" r="2.5"/><path d="M13 22c1-3 7-3 8 0M9 13V9h4M25 13V9h-4M9 21v4h4M25 21v4h-4"/></g></svg>
      <div><h2 class="service-name">Quick Admission Decisions</h2>
      <p class="service-text">CAMPUS PATH makes it easy for students by proactively contacting the universities for getting timely offers. In addition, we help resolve all minor issues in the offers.</p></div>
    </div>
  </section>

  <section class="page page--services">
    <div class="service">
      <svg class="service-icon" viewBox="0 0 34 34"><circle class="disc" cx="17" cy="17" r="17"/><g class="glyph"><path d="M11 12l6-3 6 3-6 3z"/><circle cx="17" cy="17" r="2.5"/><path d="M12 25c1-4 9-4 10 0"/></g></svg>
      <div><h2 class="service-name">University Selection</h2>
      <p class="service-text">Selecting a university involves a holistic consideration of all aspects of an educational institution including facilities and future prospects. We look at each and every detail as we guide our students.</p></div>
    </div>
    <div class="service">
      <svg class="service-icon" viewBox="0 0 34 34"><circle class="disc" cx="17" cy="17" r="17"/><g class="glyph"><path d="M12 11l5-2 5 2-5 2z"/><circle cx="17" cy="16" r="2"/><path d="M10 24l4-4h6l4 4M13 20l-2-3M21 20l2-3"/></g></svg>
      <div><h2 class="service-name">Scholarship Advice</h2>
      <p class="service-text">We help our students in advising them to various scholarships offered by universities and government sectors and assist them with the entire application process.</p></div>
    </div>
    <div class="service">
      <svg class="service-icon" viewBox="0 0 34 34"><circle class="disc" cx="17" cy="17" r="17"/><g class="glyph"><rect x="10" y="10" width="14" height="15"/><path d="M10 13h14M13 16h2M19 16h2M13 19h2M19 19h2M16 25v-3h2v3"/></g></svg>
      <div><h2 class="service-name">Accommodation</h2>
      <p class="service-text">We assist our students by providing information on various available accommodations like on campus, off campus, Homestays, Student housing, Residential accommodation so on and so forth.</p></div>
    </div>
    <div class="service">
      <svg class="service-icon" viewBox="0 0 34 34"><circle class="disc" cx="17" cy="17" r="17"/><g class="glyph"><rect x="10" y="11" width="11" height="14" rx="1"/><path d="M21 13l3 1-2 10"/><circle cx="15.5" cy="16" r="2"/><path d="M13 21h5"/></g></svg>
      <div><h2 class="service-name">Visa assistance</h2>
      <p class="service-text">Applying for visa is a critical part of overseas education preparation. Our professional consultants provide our students with a checklist for visa processing, and help them prepare for visa interviews.</p></div>
    </div>
    <div class="service">
      <svg class="service-icon" viewBox="0 0 34 34"><circle class="disc" cx="17" cy="17" r="17"/><g class="glyph"><path d="M11 23l12-12M21 9a3 3 0 0 0 4 4M11 11l12 12M9 11l2-2 2 2-2 2z"/></g></svg>
      <div><h2 class="service-name">Other Services</h2>
      <p class="service-text">Our other services include, providing assistance in organizing Insurance, airport pick-ups, pre-departure advice etc and many more information to make the journey hassle free and comfortable.</p></div>
    </div>
    <div class="service">
      <svg class="service-icon" viewBox="0 0 34 34"><circle class="disc" cx="17" cy="17" r="17"/><g class="glyph"><path d="M9 11h6a2 2 0 0 1 2 2v11a2 2 0 0 0-2-2H9zM25 11h-6a2 2 0 0 0-2 2v11a2 2 0 0 1 2-2h6z"/></g></svg>
      <div><h2 class="service-name">Languages and preparation programs</h2>
      <p class="service-text">Our tie up connections with colleges and language schools offering courses that help in meeting essential requirements at various universities helping them secure admissions for degree programs</p></div>
    </div>
  </section>
</main>
</body>
</html>
```